BRIGHTWAVE PARTNERS NAMECARD

Need to design a name card with an existing logo.

As we are professional corporate services provider our name card has to project a professional image.
Should be corporate, simple & professional.

Our corporate color is maroon red but not too dull.

Please refer to our website at www.brightwavepartners.com.sg

Would attach our logo herewith.

Front surface of namecard details:
BRIGHTWAVE PARTNERS PTE LTD
Registration No. 208731945K

Lowe Hui Ting CA (Singapore)
Director

Tel +65 6481 2957
Mobile +65 9172 3806
lowe@brightwavepartners.com.sg
www.brightwavepartners.com.sg

47 Palmer Lane
#07-14 Harbourlight Plaza
Singapore 274153

Back of namecard:-
OUR CORE SERVICES
Incorporation services
Corporate Secretarial Services
Accountancy service
Goods & Services Taxation
Corporate & Personal Taxation
Financial Reporting
Payroll Administration

AFFILIATES:
TRIVANTA CORPORATE SERVICES PTE LTD
BRIGHTWAVEREGISTRYPTE LTD
ORR MANAGEMENT SERVICES PTE LTD
DW LIM AND COMPANY PTE LTD
LEDGERWISE ACADEMY

```html
<!DOCTYPE html>
<html lang="en">
<head>
<meta charset="utf-8">
<title>Brightwave Partners Namecard</title>
<link href="https://fonts.googleapis.com/css2?family=Open+Sans:wght@400;600;700&display=swap" rel="stylesheet">
<style>
:root{
  --brand-red:#d6234a;
  --brand-black:#151515;
  --paper:#f4f4f2;
  --white:#ffffff;
  --backdrop:#e6e3de;
}
*{margin:0;padding:0;box-sizing:border-box}
html,body{width:1200px;height:780px;overflow:hidden}
body{
  background:var(--backdrop);
  font-family:"Open Sans",Arial,sans-serif;
  display:flex;align-items:center;justify-content:center;gap:32px;
}
.card{
  width:560px;height:336px;position:relative;overflow:hidden;
  box-shadow:0 6px 18px rgba(0,0,0,.18);
}

/* Front */
.card-front{background:var(--brand-red)}
.front-brand{
  position:absolute;left:0;top:0;width:100%;height:168px;background:var(--paper);
  display:flex;align-items:center;padding-left:48px;gap:16px;
}
.brand-dot{width:54px;height:54px;border-radius:50%;background:var(--brand-red);flex:none}
.brand-name{color:var(--brand-red);font-weight:600;font-size:30px;line-height:1.1;letter-spacing:1px}
.brand-name small{display:block;font-size:14px;letter-spacing:3px;margin-top:4px}
.name-band{
  position:absolute;left:0;top:168px;width:100%;height:34px;background:var(--brand-black);
  display:flex;align-items:center;padding-left:38px;color:var(--white);font-size:17px;font-weight:600;
}
.name-band .credential{font-size:12px;font-weight:400;margin-left:6px}
.name-band .divider{margin:0 8px;font-weight:400}
.name-band .role{color:var(--brand-red);font-weight:400}
.front-details{
  position:absolute;left:0;top:202px;width:100%;height:134px;
  display:flex;align-items:center;color:var(--white);
}
.address{width:250px;text-align:right;padding-right:22px;font-size:14px;line-height:1.45}
.address .reg{display:block;margin-top:6px}
.details-rule{width:1.5px;height:92px;background:var(--white)}
.contacts{padding-left:18px;list-style:none;font-size:13px;line-height:1.55}
.contacts li{display:flex;align-items:center;gap:8px}
.contact-icon{width:16px;height:14px;background:var(--white);display:flex;align-items:center;justify-content:center;flex:none}

/* Back */
.card-back{background:var(--brand-red);color:var(--white)}
.services{position:absolute;left:36px;top:26px}
.section-title{font-size:15px;font-weight:600;letter-spacing:.5px;margin-bottom:6px}
.service-list{list-style:none;font-size:13.5px;line-height:1.5}
.service-list li{display:flex;align-items:center;gap:8px}
.service-list li::before{content:"";width:9px;height:9px;border-radius:50%;background:var(--white);flex:none}
.affiliates{position:absolute;left:36px;top:212px;width:420px}
.affiliates .section-title{font-size:13px;margin-bottom:3px}
.affiliate-lines{font-size:10px;line-height:1.55;letter-spacing:.2px}
.back-rule{position:absolute;left:0;top:284px;width:100%;height:6px;background:var(--white)}
.back-footer{
  position:absolute;left:0;top:290px;width:100%;height:46px;background:var(--brand-black);
  display:flex;align-items:center;padding-left:36px;font-size:14px;color:var(--white);
}
.back-footer .domain{color:var(--brand-red)}
</style>
</head>
<body>

<section class="card card-front">
  <div class="front-brand">
    <span class="brand-dot"></span>
    <div class="brand-name">BRIGHTWAVE PARTNERS<small>PTE LTD</small></div>
  </div>
  <div class="name-band">
    Lowe Hui Ting CA<span class="credential">(Singapore)</span><span class="divider">|</span><span class="role">Director</span>
  </div>
  <div class="front-details">
    <p class="address">
      47 Palmer Lane<br>
      #07-14 Harbourlight Plaza<br>
      Singapore 274153
      <span class="reg">Registration No. 208731945K</span>
    </p>
    <span class="details-rule"></span>
    <ul class="contacts">
      <li><span class="contact-icon"><svg width="10" height="10" viewBox="0 0 10 10"><path d="M2 1h2l1 2-1.2.8a5 5 0 0 0 2.4 2.4L7 5l2 1v2a1 1 0 0 1-1 1A7 7 0 0 1 1 2a1 1 0 0 1 1-1z" fill="#d6234a"/></svg></span>+65 6481 2957</li>
      <li><span class="contact-icon"><svg width="10" height="10" viewBox="0 0 10 10"><rect x="3" y="0.5" width="4" height="9" rx="0.8" fill="#d6234a"/></svg></span>+65 9172 3806</li>
      <li><span class="contact-icon"><svg width="12" height="10" viewBox="0 0 12 10"><rect x="1" y="2" width="10" height="6.5" fill="#d6234a"/><path d="M1 2l5 4 5-4" stroke="#fff" stroke-width="1" fill="none"/></svg></span>lowe@brightwavepartners.com.sg</li>
      <li><span class="contact-icon"><svg width="10" height="10" viewBox="0 0 10 10"><circle cx="5" cy="5" r="4" fill="none" stroke="#d6234a" stroke-width="1"/><path d="M1 5h8M5 1c-2 2.5-2 5.5 0 8M5 1c2 2.5 2 5.5 0 8" stroke="#d6234a" stroke-width=".8" fill="none"/></svg></span>www.brightwavepartners.com.sg</li>
    </ul>
  </div>
</section>

<section class="card card-back">
  <div class="services">
    <h2 class="section-title">OUR CORE SERVICES</h2>
    <ul class="service-list">
      <li>Incorporation services</li>
      <li>Corporate Secretarial Services</li>
      <li>Accountancy service</li>
      <li>Goods &amp; Services Taxation</li>
      <li>Corporate &amp; Personal Taxation</li>
      <li>Financial Reporting</li>
      <li>Payroll Administration</li>
    </ul>
  </div>
  <div class="affiliates">
    <h2 class="section-title">AFFILIATES:</h2>
    <p class="affiliate-lines">
      • TRIVANTA CORPORATE SERVICES PTE LTD &nbsp;• BRIGHTWAVEREGISTRYPTE LTD<br>
      • ORR MANAGEMENT SERVICES PTE LTD &nbsp;• DW LIM AND COMPANY PTE LTD<br>
      • LEDGERWISE ACADEMY
    </p>
  </div>
  <div class="back-rule"></div>
  <div class="back-footer">www.<span class="domain">brightwavepartners</span>.com.sg</div>
</section>

</body>
</html>
```